Business Card Design Project

Keep it simple , using logo and colors that compliment. Logo on one side with complimentary back ground color. Other side, personal info with possible complimentary design/colors

Target Market(s)

we are a non for profit that will be seeking donations . Both monetary and in kind

Industry/Entity Type

Business

Font styles to use
Sans Serif

Colors

Designer to choose colors to be used in the design.

```html
<!DOCTYPE html>
<html lang="en">
<head>
<meta charset="utf-8">
<title>Lift Together – Business Card</title>
<link rel="stylesheet" href="https://fonts.googleapis.com/css2?family=Jost:wght@300;700&family=EB+Garamond:ital,wght@0,400;1,600&display=swap">
<style>
  :root {
    --navy: #2b3154;
    --ink: #232846;
    --yellow: #f4e61e;
    --paper: #ffffff;
    --backdrop: #b9b9bb;
    --edge: #1e2238;
  }
  * { box-sizing: border-box; margin: 0; padding: 0; }
  html, body { width: 1200px; height: 757px; overflow: hidden; }
  body {
    background: var(--backdrop);
    display: flex;
    flex-direction: column;
    align-items: center;
    justify-content: center;
    gap: 40px;
  }
  .card {
    position: relative;
    width: 540px;
    height: 328px;
    border: 1px solid var(--edge);
  }
  .card--front { background: var(--paper); }
  .card--back {
    background: var(--navy);
    display: flex;
    align-items: center;
    justify-content: center;
  }

  .holder {
    position: absolute;
    left: 36px;
    top: 106px;
    color: var(--ink);
  }
  .holder__name {
    font-family: "Jost", sans-serif;
    font-weight: 700;
    font-size: 25px;
    line-height: 1;
  }
  .holder__role {
    font-family: "EB Garamond", serif;
    font-style: italic;
    font-weight: 600;
    font-size: 15px;
    margin-top: 2px;
  }

  .contact {
    position: absolute;
    left: 36px;
    top: 204px;
    list-style: none;
    font-family: "EB Garamond", serif;
    font-size: 16px;
    line-height: 23px;
    color: var(--ink);
  }
  .contact__row { display: flex; }
  .contact__label { width: 20px; }
  .contact__bar { width: 12px; color: var(--ink); }

  .brand {
    display: flex;
    align-items: center;
    gap: 12px;
    font-family: "Jost", sans-serif;
    font-weight: 300;
    line-height: 1;
    white-space: nowrap;
  }
  .brand__dot {
    display: block;
    border-radius: 50%;
    background: var(--yellow);
    flex: none;
  }
  .brand--front {
    position: absolute;
    left: 318px;
    top: 146px;
    font-size: 28px;
    color: var(--navy);
  }
  .brand--front .brand__dot { width: 22px; height: 22px; }
  .brand--back {
    font-size: 38px;
    color: var(--yellow);
  }
  .brand--back .brand__dot { width: 28px; height: 28px; }
</style>
</head>
<body>
  <section class="card card--front">
    <div class="holder">
      <p class="holder__name">Your NAME</p>
      <p class="holder__role">your postion</p>
    </div>
    <ul class="contact">
      <li class="contact__row"><span class="contact__label">P</span><span class="contact__bar">|</span><span>1234 5678</span></li>
      <li class="contact__row"><span class="contact__label">F</span><span class="contact__bar">|</span><span>1234 5678</span></li>
      <li class="contact__row"><span class="contact__label">E</span><span class="contact__bar">|</span><span>yname@lifttogether.org</span></li>
      <li class="contact__row"><span class="contact__label">W</span><span class="contact__bar">|</span><span>www.lifttogether.org</span></li>
    </ul>
    <div class="brand brand--front"><span class="brand__dot"></span><span>Lift Together</span></div>
  </section>

  <section class="card card--back">
    <div class="brand brand--back"><span class="brand__dot"></span><span>Lift Together</span></div>
  </section>
</body>
</html>
```